KTM Inquiry Partners PLLC
Law Firm Conducting Investigations
KTM Inquiry Partners PLLC -
Creative Brief
Professional
Dale Morrow
Attorney
21430 SW 3rd Ave, Suite C2-418 Bellevue, WA 98006
dale@ktminquiry-example.com
www.ktminquiry-example.com
I would like the card to be simple, clean and professional. Please use color schemes that match the logo, but don't use too much gold.
The back of the card should be blank.

```html
<!DOCTYPE html>
<html lang="en">
<head>
<meta charset="utf-8">
<title>KTM Inquiry Partners PLLC – Business Card</title>
<link rel="stylesheet" href="https://fonts.googleapis.com/css2?family=Tinos&display=swap">
<style>
  :root {
    --paper: #ffffff;
    --frame: #2a2a2a;
    --gold-light: #e9c21f;
    --gold-dark: #4a3208;
    --gold-text: #8a6a2a;
    --band-grey: #9a9a9a;
    --ink-grey: #7a7a7a;
  }
  html, body {
    margin: 0;
    padding: 0;
    width: 1200px;
    height: 751px;
    overflow: hidden;
    background: var(--paper);
  }
  .card {
    position: relative;
    width: 1200px;
    height: 751px;
    font-family: "Tinos", "Times New Roman", serif;
  }
  .card-frame {
    position: absolute;
    left: 72px;
    top: 72px;
    width: 1054px;
    height: 603px;
    border: 2px solid var(--frame);
    box-sizing: border-box;
  }
  .band {
    position: absolute;
    height: 26px;
  }
  .band--top-gold {
    left: 74px; top: 74px; width: 700px;
    background: linear-gradient(to right, var(--gold-light), var(--gold-dark));
  }
  .band--top-grey {
    left: 786px; top: 74px; width: 338px;
    background: var(--band-grey);
  }
  .band--bottom-grey {
    left: 74px; top: 647px; width: 338px;
    background: var(--band-grey);
  }
  .band--bottom-gold {
    left: 424px; top: 647px; width: 700px;
    background: linear-gradient(to right, var(--gold-dark), var(--gold-light));
  }
  .brand {
    position: absolute;
    left: 150px;
    top: 322px;
    display: flex;
    align-items: center;
    gap: 26px;
  }
  .brand-square {
    width: 118px;
    height: 118px;
    background: var(--gold-text);
  }
  .brand-name {
    margin: 0;
    font-size: 42px;
    line-height: 1.1;
    font-weight: 400;
    color: var(--gold-text);
  }
  .contact {
    position: absolute;
    left: 698px;
    top: 252px;
    color: var(--ink-grey);
  }
  .contact-name {
    margin: 0;
    font-size: 36px;
    font-weight: 400;
    line-height: 1.1;
  }
  .contact-title {
    margin: 2px 0 30px;
    font-size: 27px;
    line-height: 1.2;
  }
  .contact-details {
    margin: 0;
    font-size: 24px;
    line-height: 36px;
    font-style: normal;
  }
</style>
</head>
<body>
  <main class="card">
    <div class="card-frame"></div>
    <div class="band band--top-gold"></div>
    <div class="band band--top-grey"></div>
    <div class="band band--bottom-grey"></div>
    <div class="band band--bottom-gold"></div>

    <div class="brand">
      <div class="brand-square"></div>
      <p class="brand-name">KTM Inquiry<br>Partners</p>
    </div>

    <section class="contact">
      <h1 class="contact-name">Dale Morrow</h1>
      <p class="contact-title">Attorney</p>
      <address class="contact-details">
        21430 SW 3rd Ave, Suite C2-418<br>
        Bellevue, WA 98006<br>
        Phone: 425-555-0148<br>
        Email: dale@ktminquiry-example.com<br>
        www.ktminquiry-example.com
      </address>
    </section>
  </main>
</body>
</html>
```